Luxury Candle Startup Needs Modern Packaging Box & Matching Label Design

We are Lunavale, a luxury candle company about to launch in Australia and we need a box packaging design that is modern, minimalist, and feminine. Our target audience are females, mostly mothers, within the age range of 25-45 who are looking for high quality, handmade luxurious products. Our company is going to have a large social media presence with new mothers as we are going to show our journey with starting a business whilst on maternity leave. We would like the arch shape incorporated into the box packaging as it is beautiful and symbolises moving into a new phase in life which really represents the brand. We would like for the packaging box to be a simple white box with a sleeve insert over the box with the design to make printing easier. Our colour inspiration are very earthy colours and would like the sleeve colour to be easily changed according to the scent. For example dusky rose coloured sleeve for rose patchouli and amber scent, light coffee coloured sleeve for coffee bean cacao scent etc. Please see uploaded files for inspiration, our logo, and the type of candle jars used.
The box dimensions are:
External Dimension: 95mmW x 95mmL x 116mmH
We look forward to seeing your amazing designs!

```html
<!DOCTYPE html>
<html lang="en">
<head>
<meta charset="utf-8">
<title>Lunavale Candle Box – Sleeve Design</title>
<link rel="stylesheet" href="https://fonts.googleapis.com/css2?family=Montserrat:wght@400&display=swap">
<style>
  :root {
    --backdrop: #ffffff;
    --box-white: #f3f3f3;
    --box-edge: #e2e2e2;
    --sleeve: #fafafa;
    --arch: #d3a78a;
    --arch-deep: #c89878;
    --arch-light: #dcb59c;
    --ink-on-arch: #ffffff;
    --ink-accent: #d9b39a;
  }
  * { box-sizing: border-box; margin: 0; padding: 0; }
  html, body {
    width: 1200px; height: 868px; overflow: hidden;
    background: var(--backdrop);
  }
  .net { position: relative; width: 1200px; height: 868px; }

  .panel {
    position: absolute; background: var(--box-white);
    outline: 1px solid var(--box-edge); overflow: hidden;
  }
  .panel--top   { left: 600px; top: 70px;  width: 300px; height: 300px; }
  .panel--front { left: 600px; top: 370px; width: 300px; height: 366px; }
  .panel--side  { left: 300px; top: 370px; width: 300px; height: 366px; }

  .sleeve {
    position: absolute; top: 0; bottom: 0; left: 42px; width: 228px;
    background: var(--sleeve);
  }
  .arch {
    position: absolute; left: 22px; right: 22px;
    background: linear-gradient(180deg, var(--arch) 75%, var(--arch-deep) 100%);
  }
  .panel--front .arch {
    top: 90px; bottom: 0;
    border-radius: 92px 92px 0 0;
  }
  .panel--top .arch {
    top: 0; height: 190px;
    background: linear-gradient(0deg, var(--arch-light) 0%, var(--arch) 100%);
    border-radius: 0 0 92px 92px;
  }

  .brand-name {
    position: absolute; left: 0; right: 0; text-align: center;
    font-family: "Montserrat", sans-serif; font-weight: 400;
    font-size: 20px; letter-spacing: 3px; line-height: 1;
    color: var(--ink-on-arch);
  }
  .panel--front .brand-name { bottom: 64px; }
  .panel--top .brand-name { top: 40px; transform: rotate(180deg); }

  .web-address {
    position: absolute; left: 0; right: 0; bottom: 70px; text-align: center;
    font-family: "Montserrat", sans-serif; font-weight: 400; font-size: 11px;
    letter-spacing: 1.2px; color: var(--ink-accent);
  }
</style>
</head>
<body>
  <main class="net">
    <section class="panel panel--top" aria-label="Box lid">
      <div class="sleeve">
        <div class="arch">
          <p class="brand-name">Lunavale</p>
        </div>
      </div>
    </section>

    <section class="panel panel--side" aria-label="Box side">
      <p class="web-address">www.lunavale.com.au</p>
    </section>

    <section class="panel panel--front" aria-label="Box front">
      <div class="sleeve">
        <div class="arch">
          <p class="brand-name">Lunavale</p>
        </div>
      </div>
    </section>
  </main>
</body>
</html>
```